mooncake box cover sleeve

This is a mooncake packaging box design project.
2 sizes box: 4 pcs & 6 pcs (as shown in the mock-up picture).
The length of the box is the same: 20 cm.
Dimensions, please see pictures 1 & 2.
prefer sleeve area/dimension: 20cm x 15cm
(15cm width is good to use on both boxes, IMPORTANT. please follow this scale in your design & mock up)
Product Name: Hong Kong Style Custard Mooncake with Flaky Egg Waffle Crust. 雞蛋仔酥皮奶黃月
Product Information:
Handmade Custard Mooncake.
For the Moon Festival. Once a year, to celebrate the biggest and brightest moon of the year.
Mooncakes are expensive products. For friends & family, and many businesses for their VIP customers.
Our mooncake is made with all-natural ingredients, authentic Hong Kong-style custard, using a traditional grandfather recipe, and baked with a Hong Kong-style egg waffle crust (this crust is the key and unique selling point).
Key points / must-have / need to be emphasized in this design.
- Traditional Hong Kong-style Custard
- Baked with HK-style Egg Waffle crust
- All-natural ingredients
- Luxury, high-end feel
- A full, bright moon.
- Yellow Custard
- Made in USA
- Add a line for the product name in Chinese 雞蛋仔酥皮奶黃月
I need 1 paper sleeve design that works for both boxes.
I found a company with the same concept for your reference.
See pictures 3 & 4.
**IMPORTANT** 1 sleeve works for both boxes.
Color of the box:
Open. I will order plain color. You can pick the best color to match your design.
The 4 pcs & 6 pcs can be different colors.
Preferred colors: Yellow, Black, Orange, Red tone.
NO on: Blue, purple, green, white.
Color theme of the sleeve design:
Yellow, Golden, Orange, Dark luxury, healthy earth tone, to match my logo.
This is a custard mooncake product, luxury, fine bakery products. Please give a feeling of: organic, clean, earth tone, healthy, fresh feeling.
(OK to use a little bit of green/earth tone, just to avoid Green on the plain box color)
Useful element for MoonFestival:
- Full moon
- Lantern
- Mooncake
- Family gathering
Please feel free to use all the add-on printing features to add a high-end feel. *GOLD STAMP FOIL is a must, the more the better*
Spot UV, embossed, are all welcome.
Home-Baked instructions:
We used to have a separate card, printed both sides (attached).
I would like to print this on BOTH inside the open box (see pic 2), and on the back of the sleeve. So no more cards needs to be giving out.
Please feel free to re-design a bit. thanks.
Information must have:
Front panel:
- Product Name
- Company Logo
- Egg Waffle image
- Made in California, USA (with the flag)
Back panel:
- Nutrition Fact
- Save spaces for ingredients listing (will provide later)
- Home-Baked instructions (Follow attached square card for info, make is shorter and simpler, Make it persuasive to try, give an easy feeling, Highly recommend the customer to follow)
- Fresh Baked On (A spaces for Date Stamp 2x5cm)
For details, please visit our website:
www.tessaplumOR.com
The boxes you see there are 2025.
We want a complete face lift in 2026. Thank you.
****New Message Jan 09, 2026*****
Dear all designers,
- No stock picture purchase please.
- uploaded new files for reference: please use "Lion Rock" (this one I own it, bought from previous project)
- 4 Icons must clearly shown on Front Panel.
- Space for Date Stamp.
Because this product has no preservatives, it is important to enjoy it before the date.
Please use my handwriting as a reference. Please forgive me. My drawing is not good, and please implement it with your professional skills. Without a face-to-face meeting, this is the best I can do to explain. Thanks again, all.

```html
<!DOCTYPE html>
<html lang="en">
<head>
<meta charset="utf-8">
<title>Egg Waffle Custard Mooncake Sleeve</title>
<link rel="stylesheet" href="https://fonts.googleapis.com/css2?family=EB+Garamond:ital,wght@1,400;1,500&family=Noto+Sans+TC:wght@500&display=swap">
<style>
  :root {
    --page: #ffffff;
    --rust: #c96e3b;
    --amber: #e8a048;
    --custard: #efc25e;
    --cream: #f6f0df;
    --ink: #6e3512;
    --title: #7a3e12;
    --arrow: #b45a35;
    --rule: #3a1a0c;
    --badge-ring: #f4d48a;
    --badge-face: #f7ecd6;
  }
  html, body {
    margin: 0;
    width: 1200px;
    height: 1200px;
    overflow: hidden;
    background: var(--page);
  }
  .sleeve {
    position: absolute;
    left: 4px;
    top: 103px;
    width: 1191px;
    height: 994px;
  }
  .sleeve svg { display: block; width: 100%; height: 100%; }
  .band-top { fill: var(--rust); }
  .band-mid { fill: var(--amber); }
  .band-low { fill: var(--cream); }
  .panel-rule { stroke: var(--rule); stroke-width: 2; fill: none; }
  .fold-line { stroke: var(--rule); stroke-width: 2; stroke-dasharray: 8 6; }
  .date-box { fill: var(--custard); }
  .title-zh {
    font-family: "Noto Sans TC", sans-serif;
    font-weight: 500;
    font-size: 110px;
    fill: var(--title);
    letter-spacing: 2px;
  }
  .serif {
    font-family: "EB Garamond", Georgia, serif;
    font-style: italic;
    fill: var(--ink);
  }
  .date-label { font-size: 42px; }
  .notice { font-size: 41px; }
  .callout { font-size: 42px; }
  .origin-line { font-size: 40px; }
  .batch-note { font-size: 34px; }
  .badge-ring { fill: var(--badge-ring); }
  .badge-face { fill: var(--badge-face); }
  .arrow-line { stroke: var(--arrow); stroke-width: 2; }
  .arrow-dot, .arrow-head { fill: var(--arrow); }
</style>
</head>
<body>
<div class="sleeve">
  <svg viewBox="0 0 1654 1380" xmlns="http://www.w3.org/2000/svg">
    <defs>
      <linearGradient id="productTone" x1="0" y1="0" x2="1" y2="1">
        <stop offset="0" stop-color="#f2d27e"/>
        <stop offset="1" stop-color="#e3b45a"/>
      </linearGradient>
    </defs>

    <!-- sleeve bands -->
    <path class="band-low" d="M0 0 H1654 V1330 Q1654 1380 1604 1380 H50 Q0 1380 0 1330 Z"/>
    <path class="band-mid" d="M0 373 H1654 V747 Q1654 797 1604 797 H50 Q0 797 0 747 Z"/>
    <rect class="band-top" x="0" y="0" width="1654" height="373"/>

    <!-- front panel frame -->
    <line class="panel-rule" x1="90" y1="0" x2="90" y2="797"/>
    <line class="panel-rule" x1="1570" y1="0" x2="1570" y2="797"/>
    <line class="fold-line" x1="90" y1="797" x2="1570" y2="797"/>
    <rect class="panel-rule" x="90" y="799" width="1480" height="511" rx="10"/>

    <!-- product name -->
    <text class="title-zh" x="832" y="158" text-anchor="middle">雞蛋仔酥皮奶黃月</text>

    <!-- date stamp box -->
    <rect class="date-box" x="363" y="203" width="931" height="355" rx="50"/>
    <text class="serif date-label" x="828" y="254" text-anchor="middle">Freshly Baked on:</text>
    <text class="serif notice" text-anchor="middle">
      <tspan x="828" y="402">This product contains NO PRESERVATIVES.</tspan>
      <tspan x="828" y="443">Please consume within 10 days of the above date OR</tspan>
      <tspan x="828" y="484">follow the Home-Baked method to enjoy it within 90 days</tspan>
      <tspan x="828" y="524">(Instructions Behind)</tspan>
    </text>

    <!-- feature badges -->
    <g class="badges">
      <circle class="badge-ring" cx="638" cy="676" r="82"/>
      <circle class="badge-face" cx="638" cy="676" r="62"/>
      <circle class="badge-ring" cx="834" cy="676" r="82"/>
      <circle class="badge-face" cx="834" cy="676" r="62"/>
      <rect class="badge-ring" x="961" y="600" width="158" height="154" rx="14"/>
      <rect class="badge-face" x="976" y="616" width="126" height="122" rx="12"/>
    </g>

    <!-- product photo area -->
    <rect x="562" y="830" width="430" height="295" rx="24" fill="url(#productTone)" role="img" aria-label="Photo of a whole egg waffle crust mooncake beside a cut piece showing the custard center"/>

    <!-- callouts -->
    <text class="serif callout" x="362" y="980" text-anchor="middle">Flaky Egg Waffle Crust</text>
    <line class="arrow-line" x1="192" y1="1004" x2="612" y2="1004"/>
    <circle class="arrow-dot" cx="192" cy="1004" r="7"/>
    <path class="arrow-head" d="M630 1004 L606 992 L612 1004 L606 1016 Z"/>

    <text class="serif callout" x="1246" y="978" text-anchor="middle">Hong Kong Style Custard Center</text>
    <line class="arrow-line" x1="948" y1="1004" x2="1469" y2="1004"/>
    <circle class="arrow-dot" cx="1469" cy="1004" r="7"/>
    <path class="arrow-head" d="M930 1004 L954 992 L948 1004 L954 1016 Z"/>

    <!-- origin line -->
    <text class="serif origin-line" x="828" y="1183" text-anchor="middle">All Natural Ingredients  /  Made in California, USA</text>
    <text class="serif batch-note" x="828" y="1234" text-anchor="middle">Handcrafted in small batches. Natural ingredients may vary in color and texture</text>
  </svg>
</div>
</body>
</html>
```